Mirelo Japanese Restaurant

We just want the japanese sakura background and the menu as below

Side dish :
Edamame $4
Japanese Steam Green Bean
Crab Craw $3 each
With Japanese mayo
Teriyaki Chicken stick $3 each
Chicken stick with home made teriyaki sauce
Tempura Prawns $7
With Japanese mayo
Miso Soup $3
Traditional Japanese soup
Salt and Pepper Calamari $7
With japanese mayo

Main dish:
Gyu Don $12
Bowl of steam rice topped with beef and onion simmered in a mildly sweet sauce.
Teriyaki Don $12
Bowl of steam rice topped with your choice of beef, chicken or pork and with our special Teriyaki sauce.
Vege Don $12
Bowl of steam rice with seasonal Vegetables with the special japanese sweet soy sauce.
Japanese Curry $12,(prawns $14)
Bowl of steam rice with Chicken, pork or prawn with japanese mild curry sauce.
Katsu Don $12
Bowl of steam rice topped with a deep-fried pork cutlet and egg with the japanese special sauce.
Oyako Don $12
Bowl of steam rice topped with chick and egg with japanese special sauce.
Spice Don $12
Bowl of steam rice topped with beef or chicken with japanese spice sauce.
Gingle Don $12
Bowl of steam rice topped with beef or chicken with japanese ginger sauce.
Sushi $3
Roll everyday on seasonal
ingredient.

Japanese-style sweets
Black Sesame Ice cream $4.5
Green tea Ice cream $4.5

Restaurant

```html
<!DOCTYPE html>
<html lang="en">
<head>
<meta charset="utf-8">
<title>Mirelo Japanese Restaurant – Menu</title>
<link rel="stylesheet" href="https://fonts.googleapis.com/css2?family=Questrial&family=Jost:ital,wght@0,400;0,500;1,400&family=Kaushan+Script&display=swap">
<style>
  :root{
    --backdrop:#ece6e0;
    --paper:#fbf7f5;
    --frame:#2a2a2a;
    --band:#e9dcc3;
    --band-line:#cdbb95;
    --ink:#1b1b1b;
    --muted:#3c3c3c;
    --leader:#9a9a9a;
    --accent:#d81a3c;
    --sakura:#f6e3e6;
    --sakura-deep:#efd0d6;
  }
  *{box-sizing:border-box;margin:0;padding:0}
  html,body{width:1200px;height:889px;overflow:hidden}
  body{background:var(--backdrop);position:relative;font-family:"Jost",sans-serif;color:var(--ink)}

  .menu-page{position:absolute;top:75px;width:546px;height:776px;background:var(--paper);box-shadow:0 2px 6px rgba(0,0,0,.18)}
  .menu-page--main{left:25px}
  .menu-page--side{left:625px}

  .page-frame{position:absolute;left:15px;top:17px;width:515px;height:742px;border:2px solid var(--frame);overflow:hidden}

  .sakura-backdrop{position:absolute;inset:0;
    background:
      radial-gradient(circle at 20% 20%,var(--sakura) 0 40px,transparent 90px),
      radial-gradient(circle at 70% 18%,var(--sakura-deep) 0 30px,transparent 90px),
      radial-gradient(circle at 88% 45%,var(--sakura) 0 50px,transparent 110px),
      radial-gradient(ellipse at 50% 92%,#e9e2d6 0 120px,transparent 260px),
      var(--paper)}

  .page-header{position:absolute;left:0;top:0;width:100%;height:92px;background:var(--band);border-bottom:1px solid var(--band-line)}
  .brand-dot{position:absolute;left:14px;top:18px;width:50px;height:50px;border-radius:50%;background:var(--accent)}
  .brand-name{position:absolute;left:70px;right:112px;top:8px;text-align:center;font-family:"Questrial",sans-serif;color:var(--ink);line-height:1.05}
  .brand-name .line1{display:block;font-size:31px}
  .brand-name .line2{display:block;font-size:28px}
  .header-art{position:absolute;right:0;top:0;width:110px;height:91px;background:linear-gradient(160deg,#f3ece2,#e3d5c6 60%,#cfc2b5)}

  .section-title{position:absolute;font-family:"Kaushan Script",cursive;color:var(--accent);font-size:40px;line-height:1}

  .menu-column{position:absolute;display:flex;flex-direction:column}
  .menu-item{margin-bottom:17px}
  .item-row{display:flex;align-items:flex-end;font-size:17px;font-weight:500;line-height:1.2}
  .item-leader{flex:1;border-bottom:1px solid var(--leader);margin:0 6px 5px}
  .item-each{font-style:italic;font-size:13px;margin-right:4px;align-self:flex-end;margin-bottom:2px}
  .item-note{font-style:italic;font-size:11px;font-weight:500;margin-top:2px}
  .item-desc{font-style:italic;font-size:11px;line-height:1.55;color:var(--muted);margin-top:2px}

  .food-photo{position:absolute;border-radius:8px}
  .photo-warm{background:radial-gradient(circle at 50% 55%,#c98a3c,#9a4a1e 55%,#3a1f16)}
  .photo-red{background:radial-gradient(circle at 50% 50%,#b84a28,#8c1e1a 55%,#2a1a18)}
  .photo-veg{background:radial-gradient(circle at 50% 50%,#c7814a,#a32b22 55%,#3c3830)}
  .photo-tea{background:radial-gradient(circle at 45% 50%,#9aa06a,#4d4a30 45%,#1e1c18)}

  .divider{position:absolute;height:1px;background:#555}

  .page-footer{position:absolute;left:0;bottom:0;width:100%;height:26px;background:var(--band);border-top:1px solid var(--band-line);text-align:center;font-family:"Questrial",sans-serif;font-size:12.5px;font-weight:700;letter-spacing:.2px;line-height:26px;text-transform:uppercase}
  .page-footer .sep{color:var(--accent);margin:0 5px}
</style>
</head>
<body>

<!-- Main dishes -->
<section class="menu-page menu-page--main">
  <div class="page-frame">
    <div class="sakura-backdrop" role="img" aria-label="Soft sakura blossom and mountain background"></div>

    <header class="page-header">
      <span class="brand-dot"></span>
      <h1 class="brand-name"><span class="line1">Mirelo</span><span class="line2">Japanese Restaurant</span></h1>
      <div class="header-art" role="img" aria-label="Cherry blossom branch with mountain scenery"></div>
    </header>

    <h2 class="section-title" style="left:20px;top:136px">Main Dish</h2>

    <div class="menu-column" style="left:20px;top:190px;width:214px">
      <div class="menu-item">
        <div class="item-row">Gyu Don<span class="item-leader"></span>$12</div>
        <p class="item-desc">Bowl of steam rice topped with beef and onion simmered in a mildly sweet sauce.</p>
      </div>
      <div class="menu-item">
        <div class="item-row">Teriyaki Don<span class="item-leader"></span>$12</div>
        <p class="item-desc">Bowl of steam rice topped with your choice of beef, chicken or pork and with our special Teriyaki sauce.</p>
      </div>
      <div class="menu-item">
        <div class="item-row">Vege Don<span class="item-leader"></span>$12</div>
        <p class="item-desc">Bowl of steam rice with seasonal Vegetables with the special japanese sweet soy sauce.</p>
      </div>
      <div class="menu-item">
        <div class="item-row">Japanese Curry<span class="item-leader"></span>$12</div>
        <p class="item-note">(Prawns _ $14)</p>
        <p class="item-desc">Bowl of steam rice with Chicken, pork or prawn with japanese mild curry sauce.</p>
      </div>
    </div>

    <div class="menu-column" style="left:276px;top:190px;width:214px">
      <div class="menu-item">
        <div class="item-row">Katsu Don<span class="item-leader"></span>$12</div>
        <p class="item-desc">Bowl of steam rice topped with a deep-fried pork cutlet and egg with the japanese special sauce.</p>
      </div>
      <div class="menu-item">
        <div class="item-row">Oyako Don<span class="item-leader"></span>$12</div>
        <p class="item-desc">Bowl of steam rice topped with chick and egg with japanese special sauce.</p>
      </div>
      <div class="menu-item">
        <div class="item-row">Spice Don<span class="item-leader"></span>$12</div>
        <p class="item-desc">Bowl of steam rice topped with beef or chicken with japanese spice sauce.</p>
      </div>
      <div class="menu-item">
        <div class="item-row">Gingle Don<span class="item-leader"></span>$12</div>
        <p class="item-desc">Bowl of steam rice topped with beef or chicken with japanese ginger sauce.</p>
      </div>
      <div class="menu-item">
        <div class="item-row">Sushi<span class="item-leader"></span>$3</div>
        <p class="item-desc">Roll everyday on seasonal ingredient.</p>
      </div>
    </div>

    <div class="food-photo photo-warm" style="left:20px;top:541px;width:222px;height:146px" role="img" aria-label="Photo of an oyako don rice bowl"></div>
    <div class="food-photo photo-red" style="left:268px;top:541px;width:222px;height:146px" role="img" aria-label="Photo of a beef gyu don rice bowl"></div>

    <footer class="page-footer">T14 Coral Bay Shopping Centre<span class="sep">•</span>Open 7 days a week 10am – 9pm</footer>
  </div>
</section>

<!-- Side dishes and sweets -->
<section class="menu-page menu-page--side">
  <div class="page-frame">
    <div class="sakura-backdrop" role="img" aria-label="Soft sakura blossom and mountain background"></div>

    <header class="page-header">
      <span class="brand-dot"></span>
      <h1 class="brand-name"><span class="line1">Mirelo</span><span class="line2">Japanese Restaurant</span></h1>
      <div class="header-art" role="img" aria-label="Cherry blossom branch with mountain scenery"></div>
    </header>

    <h2 class="section-title" style="left:20px;top:136px">Side Dish</h2>

    <div class="menu-column" style="left:22px;top:190px;width:248px">
      <div class="menu-item">
        <div class="item-row">Edamame<span class="item-leader"></span>$4</div>
        <p class="item-desc">Japanese steam green bean</p>
      </div>
      <div class="menu-item">
        <div class="item-row">Crab craw<span class="item-leader"></span><span class="item-each">each</span>$3</div>
        <p class="item-desc">With Japanese mayo</p>
      </div>
      <div class="menu-item">
        <div class="item-row">Teriyaki chicken stick<span class="item-leader"></span><span class="item-each">each</span>$3</div>
        <p class="item-desc">Chicken stick with home made teriyaki sauce</p>
      </div>
      <div class="menu-item">
        <div class="item-row">Tempura prawns<span class="item-leader"></span>$7</div>
        <p class="item-desc">With Japanese mayo</p>
      </div>
      <div class="menu-item">
        <div class="item-row">Miso Soup<span class="item-leader"></span>$3</div>
        <p class="item-desc">Traditional Japanese soup</p>
      </div>
      <div class="menu-item">
        <div class="item-row">Salt &amp; Pepper Calamari<span class="item-leader"></span>$7</div>
        <p class="item-desc">With japanese mayo</p>
      </div>
    </div>

    <div class="divider" style="left:22px;top:521px;width:246px"></div>

    <h2 class="section-title" style="left:22px;top:558px;font-size:31px;line-height:1.05">Japanese-style<br>sweets</h2>

    <div class="menu-column" style="left:22px;top:640px;width:248px">
      <div class="menu-item" style="margin-bottom:8px">
        <div class="item-row">Black Sesame Ice cream<span class="item-leader"></span>$4.5</div>
      </div>
      <div class="menu-item" style="margin-bottom:0">
        <div class="item-row">Green tea Ice cream<span class="item-leader"></span>$4.5</div>
      </div>
    </div>

    <div class="food-photo photo-red" style="left:296px;top:193px;width:196px;height:148px" role="img" aria-label="Photo of tempura prawn in a red bowl"></div>
    <div class="food-photo photo-veg" style="left:296px;top:365px;width:196px;height:148px" role="img" aria-label="Photo of a stir-fried side dish in a red bowl"></div>
    <div class="food-photo photo-tea" style="left:296px;top:538px;width:196px;height:150px" role="img" aria-label="Photo of green tea ice cream"></div>

    <footer class="page-footer">T14 Coral Bay Shopping Centre<span class="sep">•</span>Open 7 days a week 10am – 9pm</footer>
  </div>
</section>

</body>
</html>
```